Harbor Stoneworks Business card logo

We are a tile and natural stone installation company with an emphasis on high quality and design assistance. I prefer a black background with a graphic logo or maybe a photo that gives a feel of tile/natural stone. I like bold, but tasteful colors. Something to really catch the eye without being gaudy. The final design should convey expert quality and attention to detail.

Contact Information for Business Card

HARBOR STONEWORKS Quality Design and Installation

Font styles to use
Other font styles liked:
• Graviton, Illegal curves

Requirements
Must have
• Business card must be an eye-catcher, but tasteful.
• Information I need on the card:
• Business name and tagline
• Neil Ashcombe, owner
• Phone: (xxx) xxx-xxxx
• Email
• Website

```html
<!DOCTYPE html>
<html lang="en">
<head>
<meta charset="utf-8">
<title>Harbor Stoneworks — Business Card</title>
<link rel="stylesheet" href="https://fonts.googleapis.com/css2?family=Michroma&family=Russo+One&display=swap">
<style>
  :root {
    --backdrop: #141414;
    --card-black: #0b0b0b;
    --card-black-sheen: #3a3a3a;
    --ink-white: #f2f2f2;
    --ink-soft: #d6d6d6;
    --stone-light: #8d8f8e;
    --stone-mid: #6f716f;
    --stone-dark: #545653;
    --stone-ink: #a9aba7;
    --stone-ink-small: #9c9e9a;
  }
  * { box-sizing: border-box; margin: 0; padding: 0; }
  html, body {
    width: 1200px;
    height: 871px;
    overflow: hidden;
    background: var(--backdrop);
  }
  .canvas {
    width: 1200px;
    height: 871px;
    display: flex;
    align-items: center;
    justify-content: center;
    gap: 40px;
  }
  .card {
    position: relative;
    width: 540px;
    height: 309px;
    overflow: hidden;
  }

  /* Front side */
  .card-front {
    background: linear-gradient(115deg, var(--card-black-sheen) 0%, #1c1c1c 38%, var(--card-black) 62%);
    display: flex;
    align-items: center;
    padding: 0 30px;
  }
  .brand-block {
    width: 265px;
    padding-right: 16px;
  }
  .brand-name {
    font-family: "Russo One", sans-serif;
    font-size: 25px;
    line-height: 1.05;
    color: var(--ink-white);
    letter-spacing: 0.5px;
  }
  .brand-tagline {
    margin-top: 8px;
    font-family: "Michroma", sans-serif;
    font-size: 8.5px;
    letter-spacing: 1.2px;
    color: var(--ink-soft);
    white-space: nowrap;
  }
  .divider {
    width: 1.5px;
    height: 120px;
    background: var(--ink-soft);
    margin-right: 20px;
  }
  .contact-block {
    font-family: "Michroma", sans-serif;
    color: var(--ink-white);
  }
  .contact-name {
    font-size: 16px;
    letter-spacing: 2px;
    margin-bottom: 10px;
  }
  .contact-line {
    display: flex;
    align-items: center;
    gap: 8px;
    font-size: 11px;
    letter-spacing: 1.5px;
    margin-bottom: 7px;
    color: var(--ink-soft);
  }
  .contact-icon {
    width: 11px;
    height: 11px;
    flex: none;
  }

  /* Back side */
  .card-back {
    display: flex;
    flex-direction: column;
    justify-content: center;
    padding: 0 40px;
  }
  .stone-surface {
    position: absolute;
    inset: 0;
    background:
      radial-gradient(ellipse at 25% 30%, var(--stone-light) 0%, transparent 55%),
      radial-gradient(ellipse at 80% 75%, var(--stone-dark) 0%, transparent 60%),
      linear-gradient(160deg, var(--stone-mid), var(--stone-dark));
  }
  .back-name {
    position: relative;
    font-family: "Russo One", sans-serif;
    font-size: 46px;
    line-height: 1;
    color: var(--stone-ink);
    letter-spacing: 1px;
  }
  .back-tagline {
    position: relative;
    margin-top: 18px;
    font-family: "Michroma", sans-serif;
    font-size: 13px;
    letter-spacing: 2.5px;
    color: var(--stone-ink-small);
    white-space: nowrap;
  }
</style>
</head>
<body>
<main class="canvas">
  <section class="card card-front" aria-label="Business card front">
    <div class="brand-block">
      <div class="brand-name">HARBOR<br>STONEWORKS</div>
      <div class="brand-tagline">QUALITY DESIGN AND INSTALLATION</div>
    </div>
    <div class="divider"></div>
    <div class="contact-block">
      <div class="contact-name">YOUR NAME</div>
      <div class="contact-line">
        <svg class="contact-icon" viewBox="0 0 12 12" aria-hidden="true"><path d="M3 1l2 2.5-1.2 1.3a7 7 0 0 0 3.4 3.4L8.5 7 11 9l-1.3 2C5.5 11 1 6.5 1 2.3z" fill="currentColor"/></svg>
        000-000-0000
      </div>
      <div class="contact-line">
        <svg class="contact-icon" viewBox="0 0 12 12" aria-hidden="true"><rect x="0.5" y="2.5" width="11" height="7" fill="none" stroke="currentColor"/><path d="M0.5 2.5L6 7l5.5-4.5" fill="none" stroke="currentColor"/></svg>
        Email@
      </div>
      <div class="contact-line">
        <svg class="contact-icon" viewBox="0 0 12 12" aria-hidden="true"><circle cx="6" cy="6" r="5.2" fill="none" stroke="currentColor"/><ellipse cx="6" cy="6" rx="2.2" ry="5.2" fill="none" stroke="currentColor"/><path d="M1 6h10" stroke="currentColor"/></svg>
        WEBSITE
      </div>
    </div>
  </section>

  <section class="card card-back" aria-label="Business card back">
    <div class="stone-surface" role="img" aria-label="Weathered grey natural stone texture"></div>
    <div class="back-name">HARBOR<br>STONEWORKS</div>
    <div class="back-tagline">QUALITY DESIGN AND INSTALLATION</div>
  </section>
</main>
</body>
</html>
```